PowerPoint Presentation

We are looking for a new PPT layout template existing of a cover page, three internal pages - one with text bullets, one with a picture/information and one with more of a table for pricing information and the last a last "thank you - contact info" page. Feel free to grab any graphics from our website at www.larkhavenmetrics.com

Any product can be chosen from our products page. Colors are cyan and orange and feel free to choose darker backgrounds for the front and end page. Also included in the graphics is our new business card design.

Also note we are updating our website, and have attached a sample of how it looks for reference.

Reason: We are still looking for submissions for our PowerPoint presentation. We have increased the award amount as well.

Target Market(s)

Target market is private industry professionals, public safety organizations, and state and local government agencies.

Industry/Entity Type

Business

Colors
33a6d7
86cae6
cee9f5
f68d4d
f8ba93
fce2d4

```html
<!DOCTYPE html>
<html lang="en">
<head>
<meta charset="utf-8">
<title>Oil &amp; Gas Communications Solutions</title>
<link rel="stylesheet" href="https://fonts.googleapis.com/css2?family=Open+Sans:wght@300;400;700&display=swap">
<style>
  :root {
    --cyan: #33a6d7;
    --cyan-light: #86cae6;
    --cyan-pale: #cee9f5;
    --orange: #f68d4d;
    --text-grey: #6b6b6b;
    --brand-grey: #6d6e71;
    --white: #ffffff;
  }
  * { margin: 0; padding: 0; box-sizing: border-box; }
  html, body { width: 1200px; height: 878px; overflow: hidden; background: var(--white); }
  .slide {
    position: relative;
    width: 1200px;
    height: 878px;
    overflow: hidden;
    background: var(--white);
    font-family: "Open Sans", sans-serif;
  }
  .slide-title {
    position: absolute;
    left: 72px;
    top: 55px;
    font-size: 54px;
    font-weight: 300;
    color: var(--cyan);
    letter-spacing: -0.2px;
    white-space: nowrap;
  }
  .slide-intro {
    position: absolute;
    left: 73px;
    top: 133px;
    width: 1050px;
    font-size: 26px;
    line-height: 34px;
    font-weight: 300;
    color: var(--cyan-light);
  }
  .feature-list {
    position: absolute;
    top: 251px;
    list-style: none;
  }
  .feature-list.left { left: 73px; }
  .feature-list.right { left: 594px; }
  .feature-list li {
    position: relative;
    padding-left: 25px;
    height: 39.3px;
    font-size: 20px;
    line-height: 26px;
    font-weight: 400;
    color: var(--text-grey);
    white-space: nowrap;
  }
  .feature-list li::before {
    content: ">";
    position: absolute;
    left: 0;
    top: 0;
    font-weight: 700;
    color: var(--orange);
  }
  .brand-name {
    position: absolute;
    right: 60px;
    top: 780px;
    font-size: 26px;
    font-weight: 400;
    color: var(--brand-grey);
    letter-spacing: 0.5px;
  }
  .footer-band {
    position: absolute;
    left: 0;
    top: 829px;
    width: 1200px;
    height: 49px;
    background: linear-gradient(to bottom, var(--orange) 0%, var(--cyan) 35%, var(--cyan) 100%);
  }
</style>
</head>
<body>
  <main class="slide">
    <h1 class="slide-title">Oil &amp; Gas Communications Solutions</h1>
    <p class="slide-intro">Our broad line of fixed, mobile, carry portable and maritime systems satellite solutions are tailored to fit your unique location requirement.</p>

    <ul class="feature-list left">
      <li>Fixed Transportable Motorized Satellite Dish</li>
      <li>Communications Trailers</li>
      <li>Case Based VSAT System</li>
      <li>Remote Monitoring &amp; Control</li>
      <li>Mobile Roof Mounted VSAT Solutions</li>
    </ul>

    <ul class="feature-list right">
      <li>VoIP Phone Service over Satellite</li>
      <li>Auto-Pointing Satellite Internet Case</li>
      <li>Portable Office - Global Broadband &amp; Phone</li>
      <li>High Usage L-Band Service</li>
      <li>Satellite Phones with Internet</li>
    </ul>

    <div class="brand-name">LARKHAVEN METRICS</div>

    <div class="footer-band" role="img" aria-label="Decorative footer band in orange and cyan brand colours"></div>
  </main>
</body>
</html>
```